Tidewell Grove Vitamin C Serum

We need a product label and box designed for our Vitamin C Serum product. The label will go on a 2oz bottle and the box will hold the 2oz bottle. Attached are the box and label templates as well as a Vitamin C Serum we have with another brand.

For this brand, we're looking to have the product look high end/luxury.

Target Market(s)

40+ year old women

```html
<!DOCTYPE html>
<html lang="en">
<head>
<meta charset="utf-8">
<title>Tidewell Grove Vitamin C Serum Label</title>
<link rel="stylesheet" href="https://fonts.googleapis.com/css2?family=Cinzel:wght@400;700&family=Alegreya+SC:wght@700&family=Open+Sans:wght@400;700&family=Montserrat:wght@700&family=Tinos&family=Arimo:wght@400;700&display=swap">
<style>
  :root {
    --sun: #fdc72c;
    --ink: #111111;
    --charcoal: #2f2f2f;
    --paper: #ffffff;
  }
  * { margin: 0; padding: 0; box-sizing: border-box; }
  html, body { width: 1200px; height: 600px; overflow: hidden; background: var(--paper); }
  .label { position: relative; width: 1200px; height: 600px; background: var(--paper); color: var(--ink); overflow: hidden; }

  .c-ring { position: absolute; left: 0; top: 0; width: 1200px; height: 600px; }

  .directions { position: absolute; left: 46px; top: 88px; width: 330px; font-family: "Arimo", Arial, sans-serif; font-size: 21px; line-height: 24px; }
  .directions-title { display: inline-block; background: var(--sun); color: var(--paper); padding: 0 4px; font-size: 21px; line-height: 22px; letter-spacing: 0.5px; }

  .warnings { position: absolute; left: 46px; top: 356px; list-style: none; font-family: "Alegreya SC", Georgia, serif; font-weight: 700; font-size: 20px; line-height: 24.5px; }
  .warnings li::before { content: "•"; color: var(--sun); }
  .warnings .indent { padding-left: 16px; }

  .brand { position: absolute; left: 480px; top: 80px; width: 240px; text-align: center; font-family: "Arimo", Arial, sans-serif; color: var(--charcoal); }
  .brand-name { font-size: 24px; font-weight: 700; letter-spacing: 0.5px; }
  .brand-tier { margin-top: 28px; font-size: 24px; letter-spacing: 2px; }

  .title { position: absolute; left: 422px; top: 222px; font-family: "Cinzel", Georgia, serif; }
  .title-main { font-size: 44px; font-weight: 700; line-height: 48px; letter-spacing: 0.5px; }
  .title-letter { position: absolute; left: 203px; top: -14px; font-family: "Montserrat", Arial, sans-serif; font-size: 76px; font-weight: 700; line-height: 80px; }
  .title-rule { width: 194px; height: 2px; background: var(--ink); margin: 2px 0 4px; }
  .title-sub { font-size: 42px; line-height: 46px; }

  .features { position: absolute; left: 545px; top: 344px; list-style: none; font-family: "Tinos", "Times New Roman", serif; font-size: 22px; line-height: 23.2px; color: var(--charcoal); }
  .features li::before { content: "•"; color: var(--sun); margin-right: 8px; }

  .volume { position: absolute; left: 560px; top: 540px; font-family: "Tinos", "Times New Roman", serif; font-size: 24px; }

  .ingredients { position: absolute; left: 828px; top: 93px; width: 290px; font-family: "Open Sans", Arial, sans-serif; font-size: 13.3px; line-height: 22px; text-align: justify; }
  .ingredients strong { font-weight: 700; }

  .distributor { position: absolute; left: 828px; top: 486px; font-family: "Arimo", Arial, sans-serif; font-size: 18px; line-height: 20px; }
  .distributor strong { font-weight: 700; }
</style>
</head>
<body>
<main class="label">
  <svg class="c-ring" viewBox="0 0 1200 600" aria-hidden="true">
    <path fill="var(--sun)" fill-rule="evenodd"
      d="M 985 115 A 262 262 0 1 0 985 485 L 888 388 A 124 124 0 1 1 888 212 Z"/>
  </svg>

  <section class="directions">
    <h2 class="directions-title">DIRECTIONS:</h2>
    <p>Wash and pat skin dry.<br>Apply small amount with fingertips to freshly cleansed and toned face, neck and decollete areas (avoid direct contact with eyes).<br>Allow time to absorb prior to moisturizer application.</p>
  </section>

  <ul class="warnings">
    <li>For External use only</li>
    <li>Discontinue use if red</li>
    <li class="indent">ness or irritation occurs</li>
    <li>Avoid direct contact with eyes</li>
    <li>Keep out of reach of children</li>
    <li>Do not use if seal is damaged</li>
    <li class="indent">or missing</li>
    <li>Store in a cool, dark place</li>
  </ul>

  <div class="brand">
    <p class="brand-name">Tidewell Grove</p>
    <p class="brand-tier">PREMIUM</p>
  </div>

  <h1 class="title">
    <span class="title-main">VITAMIN</span>
    <span class="title-letter">C</span>
    <div class="title-rule"></div>
    <span class="title-sub">SERUM</span>
  </h1>

  <ul class="features">
    <li>20% Vitamin C</li>
    <li>98% Natural</li>
    <li>Hyaluronic Acid</li>
    <li>Vitamin E</li>
    <li>Organic Aloe</li>
    <li>Repair Fine Lines</li>
    <li>Younger Looking Skin</li>
  </ul>

  <p class="volume">2 Fl oz</p>

  <p class="ingredients"><strong>INGREDIENTS:</strong> Deionized Aqua (Water), Aloe Barbadensis Leaf (Aloe), Sodium Ascorbyl Phosphate (Vitamin C), Methylsulfonylmethane (MSM), Cassia Angustifolia Seed Polysaccharide (Botanical Hyaluronic Acid), Hamamelis Virginiana (Witch Hazel), Carbomer, (2s)-2-Amino-5-guanidinopentanoic Acid, Kosher Vegetable Glycerin, Simmondsia Chinensis (Jojoba Oil), Phenoxyethanol, EthylHexylGlycerin, d-alpha Tocopheryl Acetate (Vitamin E), Centella Asiatica (Gotu Kola Extract), Equisetum Arvense (Horsetail Plant Extract), Pelargonium Graveolens (Geranium Extract), Taraxacum Officinale (Dandelion Extract).</p>

  <address class="distributor" style="font-style: normal;">
    Distributed By:<br>
    <strong>Company Name</strong><br>
    Street Address, City, UT Zipcode<br>
    <strong>phone number</strong>
  </address>
</main>
</body>
</html>
```